K & D A/C Compressors' Business Card

Hello,

I need someone to create a new business card for my business. The name of my Business is: K & D A/C Compressors. I sell automotive air conditioning parts (a/c parts). I would like the business card to incorporate my logo, and to have an automotive feel to it. It is important that the business card feel like it is coming from an automotive parts business.

I already have a logo, which I will provide.

Thanks.

Project Deadline Extended Reason: I feel like extending the deadline until October 9, 2017, will allow for more time to design the business card. Thank you for your understanding. Added Monday, October 2, 2017

Target Market(s)

Consumers who need automotive a/c parts, and auto mechanics.

Industry/Entity Type

Automotive

Contact Information for Business Card

Business name: K & D A/C Compressors
Business Address: 48207 Southwest 64th Avenue, North Miami Beach, Florida 33847
Telephone: 305-642-1730
Fax: To be provided once I choose your design.
Website: www.kdcoolparts.example
Email: support@kdcoolparts.example
Names: To be provided once I choose your design.

Font styles to use
Sans Serif

Colors

Designer to choose colors to be used in the design.

Requirements
Must have
• The business card must include all of the "Business Card Details" and the logo I have uploaded.

```html
<!DOCTYPE html>
<html lang="en">
<head>
<meta charset="utf-8">
<title>K &amp; D A/C Compressors – Business Card</title>
<link href="https://fonts.googleapis.com/css2?family=Open+Sans:wght@400;600&display=swap" rel="stylesheet">
<style>
  :root {
    --backdrop: #2b2b2d;
    --card: #ffffff;
    --brand-blue: #1aa3e0;
    --brand-grey: #8d8e92;
    --text: #595a5e;
  }
  html, body {
    margin: 0;
    width: 1200px;
    height: 864px;
    overflow: hidden;
    background: var(--backdrop);
    font-family: "Open Sans", sans-serif;
  }
  .sheet {
    width: 1200px;
    height: 864px;
    display: flex;
    flex-direction: column;
    align-items: center;
    justify-content: center;
    gap: 40px;
  }
  .card {
    position: relative;
    width: 640px;
    height: 366px;
    background: var(--card);
    border-radius: 22px;
    box-sizing: border-box;
  }
  .brand {
    display: flex;
    align-items: center;
    gap: 14px;
  }
  .brand-mark {
    width: 30px;
    height: 30px;
    background: var(--brand-blue);
  }
  .brand-name {
    font-weight: 600;
    font-size: 30px;
    color: var(--brand-grey);
    letter-spacing: 0.5px;
    white-space: nowrap;
  }
  /* front */
  .card-front .brand {
    position: absolute;
    top: 150px;
    left: 0;
    right: 0;
    justify-content: center;
  }
  .card-front .website {
    position: absolute;
    bottom: 52px;
    left: 0;
    right: 0;
    margin: 0;
    text-align: center;
    font-size: 17px;
    color: var(--brand-blue);
  }
  /* back */
  .card-back .brand {
    position: absolute;
    top: 166px;
    left: 40px;
    gap: 12px;
  }
  .card-back .brand-name { font-size: 22px; }
  .card-back .brand-mark { width: 22px; height: 22px; }
  .divider {
    position: absolute;
    left: 366px;
    top: 70px;
    bottom: 70px;
    width: 2px;
    background: var(--brand-blue);
  }
  .contact {
    position: absolute;
    left: 392px;
    top: 74px;
    color: var(--text);
    font-size: 14.5px;
    line-height: 1.3;
  }
  .person-name {
    margin: 0;
    font-size: 23px;
    font-weight: 600;
    color: var(--brand-blue);
    line-height: 1.1;
  }
  .person-role { margin: 0 0 18px 6px; font-size: 15px; }
  .address { margin: 0 0 16px; font-style: normal; }
  .contact-list { list-style: none; margin: 0; padding: 0; }
  .contact-list li {
    display: flex;
    align-items: center;
    gap: 7px;
    white-space: nowrap;
  }
  .contact-list svg { width: 13px; height: 13px; flex: none; fill: var(--brand-blue); }
  .contact-list .icon-globe { fill: none; stroke: var(--brand-blue); stroke-width: 1.4; }
</style>
</head>
<body>
<main class="sheet">
  <section class="card card-front">
    <div class="brand">
      <span class="brand-mark"></span>
      <span class="brand-name">K &amp; D A/C Compressors</span>
    </div>
    <p class="website">www.kdcoolparts.example</p>
  </section>

  <section class="card card-back">
    <div class="brand">
      <span class="brand-mark"></span>
      <span class="brand-name">K &amp; D A/C Compressors</span>
    </div>
    <div class="divider"></div>
    <div class="contact">
      <h1 class="person-name">Alex Moreno</h1>
      <p class="person-role">President</p>
      <address class="address">48207 Southwest 64th Avenue,<br>North Miami Beach, Florida 33847</address>
      <ul class="contact-list">
        <li><svg viewBox="0 0 16 16"><path d="M3.5 1l3 3-1.8 1.8c.9 2 2.5 3.6 4.5 4.5L11 8.5l3 3-2 2.5C6.5 13.5 2.5 9.5 1 4z"/></svg>305-642-1730</li>
        <li><svg viewBox="0 0 16 16"><path d="M4 1h8v4H4zM1 6h14v6h-3v3H4v-3H1zm4 4v4h6v-4z"/></svg>305-642-1795</li>
        <li><svg viewBox="0 0 16 16"><path d="M1 3h14v10H1zm1.5 1.2L8 8.5l5.5-4.3z"/></svg>support@kdcoolparts.example</li>
        <li><svg class="icon-globe" viewBox="0 0 16 16"><circle cx="8" cy="8" r="6.5"/><ellipse cx="8" cy="8" rx="2.8" ry="6.5"/><path d="M1.5 8h13"/></svg>www.kdcoolparts.example</li>
      </ul>
    </div>
  </section>
</main>
</body>
</html>
```